Website for Ferncliff Servicemen Club

Hi I require a website design in WordPress.

It is for a Diggers Club (KMU or Club, Hotel/Restaurant).

It will have a section for the club with blogs and news as well as announcements of upcoming events on the front page.

Another major component of the site will be the Chinese restaurant which will have information about the restaurant as well as the ability to order food online (using a eCommerce module at this stage).

I have included the logos for the shop, as well as some hand drawn images that the Chinese restaurant will want included into their page. This may require a vector to be created that is of the same image (must be EXACTLY the same as the images are highly symbolic).

I am happy to increase the budget to include this vector graphic creation upon request and successful submission.

It would be desired for this to be delivered as coded HTML/CSS or Wordpress, however this is negotiable.

Hi all, thanks for the great submissions,.

Just to clarify. This is a pub (hotel, or ex-services club) that has a restaurant. The restaurant is an important aspect the the site, but not the only focus.

Unfortunately the client has offered very little directly, however the front page will need to be a balance of the Resaurant, bar, and the community sentiment of being a ex-services club, I have added some extra images. These may not suiit the website, but show what an kmu is.

Locals who are looking for a nice place to drink, or good quality food.

Restaurant

```html
<!DOCTYPE html>
<html lang="en">
<head>
<meta charset="utf-8">
<title>Ferncliff Servicemen Club</title>
<link href="https://fonts.googleapis.com/css2?family=PT+Serif&family=Arimo:ital,wght@0,400;0,700;1,400&display=swap" rel="stylesheet">
<style>
:root{
  --ink:#1f1612;
  --ink-deep:#160f0c;
  --gold:#f5c400;
  --gold-light:#ffe14a;
  --orange:#e2530d;
  --orange-text:#e0520e;
  --red:#a10d1c;
  --grey:#777;
  --muted:#8f8580;
  --rule:#d9d9d9;
  --white:#fff;
}
*{margin:0;padding:0;box-sizing:border-box}
html,body{width:750px;height:1200px;overflow:hidden;background:var(--white)}
body{position:relative;font-family:"Arimo",Arial,sans-serif;color:var(--grey)}
.abs{position:absolute}
.serif{font-family:"PT Serif",Georgia,serif}

/* header */
.site-header{left:0;top:0;width:750px;height:50px;background:var(--ink)}
.brand{left:108px;top:12px;display:flex;align-items:center;gap:6px}
.brand-name{font-family:"PT Serif",Georgia,serif;font-size:15px;color:var(--gold);line-height:1.1;width:120px}
.brand-dot{width:14px;height:14px;border-radius:50%;background:var(--orange)}
.contact{top:16px;font-family:"PT Serif",Georgia,serif;font-size:8px;color:#d8d0c8;display:flex;align-items:center;gap:5px}
.main-nav{left:0;top:50px;width:750px;height:31px;background:linear-gradient(#ffd900,#f2b400);display:flex;padding-left:133px;gap:0}
.main-nav a{font-family:"PT Serif",Georgia,serif;font-size:8px;color:#2a1a08;text-decoration:none;line-height:31px}

/* hero */
.hero{left:0;top:81px;width:750px;height:302px;background:radial-gradient(ellipse at 45% 45%,#e9a66a 0%,#d4b896 35%,#b9c3cf 70%,#9aaabb 100%)}
.hero-caption{left:108px;top:267px;width:317px;height:86px;background:rgba(20,14,10,.82);padding:12px 17px}
.hero-caption h1{font-family:"PT Serif",Georgia,serif;font-weight:400;font-size:14px;color:var(--gold);margin-bottom:6px}
.hero-caption p{font-size:7.2px;line-height:13.5px;color:var(--white)}
.hero-arrow{top:327px;width:25px;height:26px;background:var(--orange);display:flex;align-items:center;justify-content:center}

/* events */
.events{left:0;top:383px;width:750px;height:210px;background:var(--ink)}
.section-title{font-family:"PT Serif",Georgia,serif;font-size:12px;color:var(--gold)}
.event{top:59px;width:150px;text-align:center}
.event-thumb{width:53px;height:53px;border-radius:50%;margin:0 auto 15px;border:2px solid #fff}
.event h3{font-weight:400;font-size:7px;color:var(--gold);margin-bottom:5px}
.event time{display:block;font-size:6px;color:var(--orange);margin-bottom:6px}
.event p{font-size:5.6px;line-height:11px;color:var(--muted)}

/* news & posts */
.heading-orange{font-family:"PT Serif",Georgia,serif;font-size:12px;color:var(--orange-text)}
.news-img{left:108px;top:644px;width:173px;height:93px;background:linear-gradient(135deg,#f0e6d8,#a45a2c 45%,#e8c040 60%,#6f9a3c 85%)}
.post-title{font-size:7.2px;color:var(--orange-text)}
.posted{font-style:italic;font-size:6px;color:#333}
.post-text{font-size:6px;line-height:12px;color:var(--grey)}
.btn-orange{background:linear-gradient(#f06818,#d94c08);color:var(--white);font-size:7.2px;text-align:center;border-radius:2px}
.post{width:152px;height:76px;border-bottom:1px solid var(--rule)}
.date-box{left:0;top:4px;width:37px;height:35px;background:var(--orange);color:#fff;text-align:center;padding-top:4px}
.date-box b{display:block;font-weight:400;font-size:11px}
.date-box span{font-size:8px}
.post .body{left:47px;top:0;width:105px}

/* restaurant band */
.restaurant{left:0;top:871px;width:750px;height:190px;background:var(--red);text-align:center}
.restaurant-deco{left:260px;top:10px;width:230px;height:170px;border-radius:50%;background:radial-gradient(circle,rgba(255,255,255,.09),rgba(255,255,255,0) 70%)}
.restaurant h2{position:absolute;left:0;top:21px;width:750px;font-weight:400;font-size:14px;color:var(--white)}
.restaurant p{position:absolute;left:145px;top:57px;width:460px;font-size:6.7px;line-height:15px;color:var(--white)}
.btn-gold{left:291px;top:130px;width:167px;height:31px;background:linear-gradient(#ffe200,#f2b600);color:#3a2000;font-size:7.2px;line-height:31px;border-radius:2px}

/* footer */
.site-footer{left:0;top:1061px;width:750px;height:112px;background:var(--ink)}
.foot-col{top:24px}
.foot-col h4{font-family:"PT Serif",Georgia,serif;font-weight:400;font-size:10px;color:var(--gold);margin-bottom:5px}
.foot-col li{list-style:none;font-size:4.8px;line-height:9.6px;color:#e0d8d0}
.field{width:98px;height:11px;background:#120c09;margin-bottom:5px;font-size:4.8px;color:#e0d8d0;padding:3px 4px}
.signup{margin-left:58px;width:40px;height:11px;background:var(--gold);font-size:5px;color:#3a2000;text-align:center;line-height:11px}
.bottom-bar{left:0;top:1173px;width:750px;height:27px;background:var(--ink-deep);font-size:5px;color:#e0d8d0}
.social{width:13px;height:13px;border-radius:50%;background:#6a605a;top:7px}
</style>
</head>
<body>

<header class="site-header abs">
  <div class="brand abs"><span class="brand-name">Ferncliff Servicemen Club</span><span class="brand-dot"></span></div>
  <div class="contact abs" style="left:423px">
    <svg width="12" height="12" viewBox="0 0 12 12"><rect x="1" y="1" width="4" height="10" rx="1" fill="#f5c400"/><rect x="6" y="3" width="5" height="8" rx="1" fill="none" stroke="#f5c400"/></svg>
    ( 1034 ) 555 218
  </div>
  <div class="contact abs" style="left:511px">
    <svg width="10" height="12" viewBox="0 0 10 12"><path d="M5 11C2 7 1 5.5 1 4a4 4 0 0 1 8 0c0 1.5-1 3-4 7z" fill="none" stroke="#f5c400"/><circle cx="5" cy="4" r="1.4" fill="#f5c400"/></svg>
    102 street name, City name,Country
  </div>
</header>

<nav class="main-nav abs">
  <a href="#" style="width:62px">HOME</a><a href="#" style="width:66px">ABOUT</a><a href="#" style="width:117px">CUSTOMER SERVICE</a><a href="#" style="width:60px">BLOG</a><a href="#" style="width:61px">NEWS</a><a href="#" style="width:69px">EVENTS</a><a href="#">CONTACT US</a>
</nav>

<section class="hero abs" role="img" aria-label="Plated noodle dish with chicken, peppers and carrots"></section>
<div class="hero-caption abs">
  <h1>Ferncliff Club, Hotel &amp; Restaurant.</h1>
  <p>default model text, and a search for 'lorem ipsum' will uncover many web sites still in their infancy. Various versions have evolved over the years, sometimes by accident, sometimes on purpose</p>
</div>
<div class="hero-arrow abs" style="left:590px"><svg width="8" height="12"><path d="M6 1L1 6l5 5" stroke="#fff" fill="none" stroke-width="1.3"/></svg></div>
<div class="hero-arrow abs" style="left:617px"><svg width="8" height="12"><path d="M2 1l5 5-5 5" stroke="#fff" fill="none" stroke-width="1.3"/></svg></div>

<section class="events abs">
  <h2 class="section-title abs" style="left:0;top:22px;width:750px;text-align:center;font-weight:400">Upcoming events</h2>
  <svg class="abs" style="left:99px;top:92px" width="10" height="24"><path d="M9 1L1 12l8 11" stroke="#5a4e48" fill="none"/></svg>
  <svg class="abs" style="left:646px;top:92px" width="10" height="24"><path d="M1 1l8 11-8 11" stroke="#5a4e48" fill="none"/></svg>
  <article class="event abs" style="left:132px">
    <div class="event-thumb" role="img" aria-label="Guests at the club bar" style="background:radial-gradient(#8a3a30,#3a2a28)"></div>
    <h3>Default model text, and a search</h3><time>28 March 2014</time>
    <p>Dfault model text, and a search for 'lorem ipsum' will uncover many web sites still in their infancy. Various versions...</p>
  </article>
  <article class="event abs" style="left:303px">
    <div class="event-thumb" role="img" aria-label="Plated seafood dish" style="background:radial-gradient(#f4e2b0,#e89a20)"></div>
    <h3>Default model text, and a search</h3><time>28 March 2014</time>
    <p>Dfault model text, and a search for 'lorem ipsum' will uncover many web sites still in their infancy. Various versions...</p>
  </article>
  <article class="event abs" style="left:475px">
    <div class="event-thumb" role="img" aria-label="Meatballs with fries and salad" style="background:radial-gradient(#8a4a28,#e8c050 70%,#f4efe8)"></div>
    <h3>Default model text, and a search</h3><time>28 March 2014</time>
    <p>Dfault model text, and a search for 'lorem ipsum' will uncover many web sites still in their infancy. Various versions...</p>
  </article>
</section>

<h2 class="heading-orange abs" style="left:108px;top:616px;font-weight:400">News &amp; Announcements</h2>
<svg class="abs" style="left:267px;top:620px" width="14" height="8"><path d="M4 1L1 4l3 3M10 1l3 3-3 3" stroke="#999" fill="none"/></svg>
<div class="news-img abs" role="img" aria-label="Meatballs with fries and green salad"></div>
<div class="abs" style="left:108px;top:749px;width:175px">
  <div class="post-title">Lorem Ipsum as their default model text</div>
  <div class="posted" style="margin-top:7px">Posted on 27 Febr 2014</div>
  <p class="post-text" style="margin-top:6px">Lorem Ipsum as their default model text, and a search for 'lorem ipsum' will uncover many web sites still in their infancy. Various versions have evolved...</p>
</div>
<a class="btn-orange abs" style="left:108px;top:825px;width:130px;height:22px;line-height:22px">View News &amp; Announcements</a>

<h2 class="heading-orange abs" style="left:306px;top:616px;font-weight:400">Recent Posts</h2>
<div class="abs" style="left:473px;top:641px;width:1px;height:68px;background:var(--rule)"></div>
<div class="abs" style="left:473px;top:728px;width:1px;height:68px;background:var(--rule)"></div>

<article class="post abs" style="left:306px;top:641px"><div class="date-box abs"><b>27</b><span>Feb</span></div><div class="body abs"><div class="post-title">Lorem Ipsum as their default</div><div class="posted" style="margin-top:6px">Posted on 27 Febr 2014</div><p class="post-text" style="margin-top:4px">Lorem Ipsum as their default model text, and a search for 'lorem ipsum' will uncover many web sites...</p></div></article>
<article class="post abs" style="left:489px;top:641px"><div class="date-box abs"><b>27</b><span>Feb</span></div><div class="body abs"><div class="post-title">Lorem Ipsum as their default</div><div class="posted" style="margin-top:6px">Posted on 27 Febr 2014</div><p class="post-text" style="margin-top:4px">Lorem Ipsum as their default model text, and a search for 'lorem ipsum' will uncover many web sites...</p></div></article>
<article class="post abs" style="left:306px;top:728px"><div class="date-box abs"><b>27</b><span>Feb</span></div><div class="body abs"><div class="post-title">Lorem Ipsum as their default</div><div class="posted" style="margin-top:6px">Posted on 27 Febr 2014</div><p class="post-text" style="margin-top:4px">Lorem Ipsum as their default model text, and a search for 'lorem ipsum' will uncover many web sites...</p></div></article>
<article class="post abs" style="left:489px;top:728px"><div class="date-box abs"><b>27</b><span>Feb</span></div><div class="body abs"><div class="post-title">Lorem Ipsum as their default</div><div class="posted" style="margin-top:6px">Posted on 27 Febr 2014</div><p class="post-text" style="margin-top:4px">Lorem Ipsum as their default model text, and a search for 'lorem ipsum' will uncover many web sites...</p></div></article>
<a class="btn-orange abs" style="left:512px;top:819px;width:130px;height:23px;line-height:23px">View all Posts</a>

<section class="restaurant abs">
  <div class="restaurant-deco abs" role="img" aria-label="Faint ornamental motif of the Chinese restaurant"></div>
  <h2 class="serif">Our Chinese restaurant</h2>
  <p>It is a long established fact that a reader will be distracted by the readable content of a page when looking at its layout. The point of using Lorem Ipsum is that it has a more-or-less normal distribution of letters, as opposed to using 'Content here, content here', making it look like readable English. Many desktop publishing packages and web page editors now use Lorem Ipsum as their default model text, and a search for 'lorem ipsum' will uncover many web sites still in their infancy...</p>
  <a class="btn-gold abs">Click here for our Chinese restaurant</a>
</section>

<footer class="site-footer abs">
  <div class="foot-col abs" style="left:117px"><h4>Welcome</h4><ul><li>HOME</li><li>ABOUT</li><li>CUSTOMER SERVICE</li><li>BLOG</li><li>NEWS</li><li>EVENTS</li><li>CONTACT US</li></ul></div>
  <div class="foot-col abs" style="left:202px"><h4>Customer Service</h4><ul><li>HELP CENTER</li><li>CONTACT US</li><li>SIZE CHARTS</li><li>RETURN POLICY</li><li>SITE MAP</li></ul></div>
  <div class="foot-col abs" style="left:326px"><h4>Locations</h4><ul><li>VARIOUS VERSIONS HAVE</li><li>VARIOUS VERSIONS HAVE EVOLVED</li><li>VARIOUS</li><li>VARIOUS VERSIONS HAVE EVO</li><li>VARIOUS VERSIONS</li><li>VARIOUS VERSIONS HAVE EVOLVED</li></ul></div>
  <div class="foot-col abs" style="left:433px"><h4>Events</h4><ul><li>SIGN IN</li><li>TRACK MY ORDER</li><li>HELP</li></ul></div>
  <div class="foot-col abs" style="left:518px"><h4>Newsletter Signup</h4><div class="field">NAME :</div><div class="field">EMAIL :</div><div class="signup">SIGNUP</div></div>
</footer>

<div class="bottom-bar abs">
  <span class="abs" style="left:115px;top:11px">COPYRIGHT © 2014. FERNCLIFF. ALL RIGHTS RESERVED.</span>
  <span class="abs" style="left:522px;top:11px">FOLLOW US :</span>
  <span class="social abs" style="left:558px"></span>
  <span class="social abs" style="left:574px"></span>
  <span class="social abs" style="left:590px"></span>
  <span class="social abs" style="left:606px"></span>
</div>

</body>
</html>
```